International wholesale business needs a business card

We need a business card.

Company Details:
Company Name and logo
Address, Phone number, Website
Employee Details:
Name, Designation, Mobile Number & Email address

```html
<!DOCTYPE html>
<html lang="en">
<head>
<meta charset="utf-8">
<title>Corvane Trading – Business Card</title>
<link rel="stylesheet" href="https://fonts.googleapis.com/css2?family=Playfair+Display:wght@500&family=Montserrat:wght@400;500&display=swap">
<style>
  :root {
    --bg: #e4e4e4;
    --card-white: #ffffff;
    --brand-red: #c1272d;
    --brand-grey: #8a9096;
    --text-grey: #5f6469;
    --back-grey: #8b9197;
    --stripe-grey: #9aa0a6;
  }
  * { box-sizing: border-box; margin: 0; padding: 0; }
  html, body { width: 1200px; height: 800px; overflow: hidden; }
  body {
    background: var(--bg);
    display: flex;
    align-items: center;
    justify-content: center;
    gap: 50px;
    font-family: "Montserrat", Arial, sans-serif;
  }
  .card {
    position: relative;
    width: 530px;
    height: 302px;
    border-radius: 22px;
    overflow: hidden;
    box-shadow: 0 10px 24px rgba(0,0,0,0.18);
  }
  .card--front { background: var(--card-white); }
  .card--back {
    background: var(--back-grey);
    display: flex;
    align-items: center;
    justify-content: center;
  }
  .front-wave { position: absolute; inset: 0; width: 100%; height: 100%; }
  .brand {
    display: flex;
    align-items: center;
    gap: 12px;
  }
  .brand-mark {
    width: 34px; height: 34px;
    border-radius: 50%;
    border: 4px solid var(--brand-grey);
    flex: none;
  }
  .brand-name {
    font-family: "Playfair Display", Georgia, serif;
    font-weight: 500;
    text-transform: uppercase;
    letter-spacing: 1px;
    line-height: 1.05;
  }
  .card--front .brand {
    position: absolute;
    left: 28px;
    top: 150px;
  }
  .card--front .brand-name {
    color: var(--brand-red);
    font-size: 24px;
    display: flex;
    flex-direction: column;
  }
  .card--back .brand-mark { width: 54px; height: 54px; border: 6px solid #ffffff; }
  .card--back .brand-name { color: #ffffff; font-size: 42px; }
  .contact {
    position: absolute;
    left: 222px;
    top: 26px;
    color: var(--text-grey);
  }
  .contact-name {
    font-family: "Playfair Display", Georgia, serif;
    font-weight: 500;
    font-size: 20px;
    letter-spacing: 0.5px;
    text-transform: uppercase;
    color: var(--text-grey);
    line-height: 1.2;
  }
  .contact-role {
    font-size: 11.5px;
    color: var(--brand-red);
    margin: 1px 0 8px;
  }
  .contact-list { list-style: none; font-size: 10.5px; line-height: 1.4; }
  .contact-list li { display: flex; align-items: flex-start; gap: 7px; }
  .contact-list svg { width: 10px; height: 10px; margin-top: 2px; flex: none; fill: var(--brand-red); }
</style>
</head>
<body>

<section class="card card--front" aria-label="Business card front">
  <svg class="front-wave" viewBox="0 0 530 302" preserveAspectRatio="none" aria-hidden="true">
    <path d="M0,264 C236,260 432,224 524,92" fill="none" stroke="var(--stripe-grey)" stroke-width="6"/>
    <path d="M0,278 C240,274 440,240 530,110 L530,302 L0,302 Z" fill="var(--brand-red)"/>
  </svg>

  <div class="brand">
    <span class="brand-mark"></span>
    <span class="brand-name"><span>Corvane</span><span>Trading</span></span>
  </div>

  <div class="contact">
    <h1 class="contact-name">Daniel Reyes</h1>
    <p class="contact-role">President</p>
    <ul class="contact-list">
      <li>
        <svg viewBox="0 0 10 10"><path d="M5 0a3.5 3.5 0 0 0-3.5 3.5C1.5 6 5 10 5 10s3.5-4 3.5-6.5A3.5 3.5 0 0 0 5 0zm0 5a1.5 1.5 0 1 1 0-3 1.5 1.5 0 0 1 0 3z"/></svg>
        <span>1420 Harbor View Road<br>Juneau, Alaska 99801</span>
      </li>
      <li>
        <svg viewBox="0 0 10 10"><path d="M2 0l2 2.5-1 1.2c.6 1.3 1.7 2.4 3 3l1.2-1L10 8l-1.4 1.8C4.5 9.6.4 5.5.2 1.4z"/></svg>
        <span>555-310-4821</span>
      </li>
      <li>
        <svg viewBox="0 0 10 10"><path d="M2.5 0h5v10h-5zM3.5 1v7h3V1z"/></svg>
        <span>555-310-4977</span>
      </li>
      <li>
        <svg viewBox="0 0 10 10"><path d="M0 2h10v6H0zm1 1v.3l4 2.5 4-2.5V3z"/></svg>
        <span>info@corvanetrading.com</span>
      </li>
      <li>
        <svg viewBox="0 0 10 10"><circle cx="5" cy="5" r="4.2" fill="none" stroke="var(--brand-red)" stroke-width="1.2"/><path d="M1 5h8M5 1c-2 2.5-2 5.5 0 8M5 1c2 2.5 2 5.5 0 8" fill="none" stroke="var(--brand-red)" stroke-width="0.8"/></svg>
        <span>corvanetrading.com</span>
      </li>
    </ul>
  </div>
</section>

<section class="card card--back" aria-label="Business card back">
  <div class="brand">
    <span class="brand-mark"></span>
    <span class="brand-name">Corvane Trading</span>
  </div>
</section>

</body>
</html>
```